Need a label for food product looking original design

We need two labels designed ( Front and Back ) for our new product Freeze Dried Strawberry Pieces On the front should also be our company name Velmora . A pack will weigh 50 grams there should also be an image included of these strawbberies please find an attached file. Also it's suitable for vegans and vegetarians On the back there should be some information included what the product is used for and nutritional facts, also an e-mail for questions or product quality to be sent to sales@velmora.co.uk Both labels should be 16cm long and 11cm wide we'll be using stand up pouches.

Target Market(s)

Bakery, snacks.

Font styles to use
Decorative
Script

Requirements
Must have
• Company name, image of the product.Label color to blend in pouch color.
Nice to have
• Suitable for vegans and vegetarians logos.
Should not have
• Custom printed pouches are not available.

```html
<!DOCTYPE html>
<html lang="en">
<head>
<meta charset="UTF-8">
<title>Velmora Strawberry Pieces – Front Label</title>
<link rel="stylesheet" href="https://fonts.googleapis.com/css2?family=Oswald:wght@500;600&family=Lato:wght@400;700&display=swap">
<style>
  :root {
    --pouch-white: #f7f7f7;
    --ink: #161616;
    --berry-red: #d0213f;
    --berry-deep: #7e1628;
    --berry-mid: #b0283e;
    --leaf-green: #3a8a3a;
    --badge-line: #2a2a2a;
  }
  * { margin: 0; padding: 0; box-sizing: border-box; }
  html, body {
    width: 900px;
    height: 1200px;
    overflow: hidden;
    background: var(--pouch-white);
  }
  .label {
    position: relative;
    width: 900px;
    height: 1200px;
    background: var(--pouch-white);
    font-family: "Lato", sans-serif;
    color: var(--ink);
  }
  .brand-name {
    position: absolute;
    top: 118px;
    left: 0;
    width: 100%;
    text-align: center;
    font-weight: 400;
    font-size: 56px;
    letter-spacing: 0.5px;
  }
  .product-title {
    position: absolute;
    top: 238px;
    left: 66px;
    font-family: "Oswald", sans-serif;
    font-weight: 600;
    font-size: 140px;
    line-height: 1.05;
    letter-spacing: 2px;
    text-transform: uppercase;
  }
  .product-process {
    position: absolute;
    top: 545px;
    left: 70px;
    font-size: 48px;
    letter-spacing: 1px;
    color: var(--berry-red);
    text-transform: uppercase;
  }
  .claims {
    position: absolute;
    top: 690px;
    left: 66px;
    list-style: none;
  }
  .claims li {
    display: flex;
    align-items: center;
    gap: 18px;
    font-size: 30px;
    letter-spacing: 0.5px;
    text-transform: uppercase;
    height: 62px;
  }
  .claims svg { width: 34px; height: 38px; flex: none; }
  .product-photo {
    position: absolute;
    top: 470px;
    left: 470px;
    width: 400px;
    height: 620px;
    background:
      radial-gradient(ellipse 42% 28% at 60% 30%, var(--berry-mid) 0%, var(--berry-deep) 60%, rgba(126,22,40,0) 100%),
      radial-gradient(ellipse 45% 24% at 45% 70%, var(--berry-mid) 0%, var(--berry-deep) 60%, rgba(126,22,40,0) 100%);
  }
  .diet-badge {
    position: absolute;
    top: 930px;
    left: 82px;
    width: 185px;
    height: 185px;
    border-radius: 50%;
    border: 3px solid var(--badge-line);
    background: #ffffff;
  }
  .net-weight {
    position: absolute;
    top: 1098px;
    left: 345px;
    font-family: "Oswald", sans-serif;
    font-weight: 500;
    font-size: 42px;
  }
</style>
</head>
<body>
  <main class="label">
    <div class="brand-name">Velmora</div>

    <h1 class="product-title">Strawberry<br>Pieces</h1>
    <div class="product-process">Freeze Dried</div>

    <ul class="claims">
      <li>
        <svg viewBox="0 0 34 38" aria-hidden="true"><path d="M17 8 C5 8 2 16 4 23 C7 31 13 36 17 37 C21 36 27 31 30 23 C32 16 29 8 17 8 Z" fill="var(--berry-red)"/><path d="M10 4 L17 9 L24 4 L21 10 L13 10 Z" fill="var(--leaf-green)"/></svg>
        No added sugar.
      </li>
      <li>
        <svg viewBox="0 0 34 38" aria-hidden="true"><path d="M17 8 C5 8 2 16 4 23 C7 31 13 36 17 37 C21 36 27 31 30 23 C32 16 29 8 17 8 Z" fill="var(--berry-red)"/><path d="M10 4 L17 9 L24 4 L21 10 L13 10 Z" fill="var(--leaf-green)"/></svg>
        No preservatives.
      </li>
      <li>
        <svg viewBox="0 0 34 38" aria-hidden="true"><path d="M17 8 C5 8 2 16 4 23 C7 31 13 36 17 37 C21 36 27 31 30 23 C32 16 29 8 17 8 Z" fill="var(--berry-red)"/><path d="M10 4 L17 9 L24 4 L21 10 L13 10 Z" fill="var(--leaf-green)"/></svg>
        100% Strawberry.
      </li>
    </ul>

    <div class="product-photo" role="img" aria-label="Scattered freeze dried strawberry pieces"></div>

    <div class="diet-badge" role="img" aria-label="Suitable for vegans and vegetarians badge"></div>

    <div class="net-weight">Net Wt 50g</div>
  </main>
</body>
</html>
```